La etiqueta deberá contener lo siguiente:
-Titulo: Miel de Agave Kosher
-Logo de VORET (realizado por ustedes, adjunto diseño)
-Logo del certificado: KOSHER (Se adjuntan certificado)
-Mililitros: 750 ml
-Información nutrimental: se adjunta tabla
La miel deberá sobresalir de las demás por el estilo lujoso y llamativo de la etiqueta.

```html
<!DOCTYPE html>
<html lang="es">
<head>
<meta charset="utf-8">
<title>Miel de Agave Kosher — Etiqueta</title>
<link rel="stylesheet" href="https://fonts.googleapis.com/css2?family=Montserrat:wght@400;700&family=Arimo:wght@400;700&display=swap">
<style>
  :root {
    --page: #ffffff;
    --label-black: #0b0b0b;
    --gold-deep: #c9951c;
    --gold: #e6bb2a;
    --gold-light: #f7dc4a;
    --muted-grey: #5a5a5a;
    --table-line: #e8e8e8;
    --table-text: #d6d6d6;
  }
  html, body {
    margin: 0;
    padding: 0;
    width: 1200px;
    height: 1200px;
    overflow: hidden;
    background: var(--page);
  }
  .canvas {
    position: relative;
    width: 1200px;
    height: 1200px;
  }
  .label {
    position: absolute;
    left: 20px;
    top: 309px;
    width: 1160px;
    height: 583px;
  }
  .brand-name {
    font-family: "Montserrat", sans-serif;
    font-weight: 400;
    font-size: 48px;
    letter-spacing: 9px;
    fill: var(--gold);
  }
  .product-title {
    font-family: "Montserrat", sans-serif;
    font-weight: 700;
    font-size: 64px;
    letter-spacing: 17px;
    fill: var(--gold);
  }
  .volume {
    font-family: "Arimo", sans-serif;
    font-size: 24px;
    fill: var(--muted-grey);
  }
  .distributor {
    font-family: "Arimo", sans-serif;
    font-size: 25px;
    fill: var(--muted-grey);
  }
  .nutrition-title {
    font-family: "Arimo", sans-serif;
    font-weight: 700;
    font-size: 27px;
    fill: var(--table-text);
  }
  .nutrition-row {
    font-family: "Arimo", sans-serif;
    font-size: 10px;
    fill: var(--table-text);
  }
  .nutrition-row.strong { font-weight: 700; }
  .nutrition-value { text-anchor: end; }
</style>
</head>
<body>
<main class="canvas">
  <svg class="label" viewBox="0 0 1483 745" xmlns="http://www.w3.org/2000/svg" role="group" aria-label="Etiqueta Miel de Agave Kosher">
    <defs>
      <linearGradient id="gold-sheen" x1="0" y1="0" x2="1" y2="1">
        <stop offset="0" style="stop-color: var(--gold-deep)"/>
        <stop offset="0.5" style="stop-color: var(--gold-light)"/>
        <stop offset="1" style="stop-color: var(--gold-deep)"/>
      </linearGradient>
    </defs>

    <!-- label band -->
    <rect class="gold-stripe" x="0" y="23" width="1483" height="22" fill="url(#gold-sheen)"/>
    <rect class="black-band" x="0" y="45" width="1483" height="655" style="fill: var(--label-black)"/>
    <rect class="gold-stripe" x="0" y="700" width="1483" height="23" fill="url(#gold-sheen)"/>

    <!-- central hexagon -->
    <polygon class="hex-frame" points="525,5 955,5 1165,373 955,740 525,740 315,373" fill="url(#gold-sheen)"/>
    <polygon class="hex-field" points="531,15 949,15 1153,373 949,730 531,730 327,373" style="fill: var(--label-black)"/>
    <polygon class="hex-inner-line" points="537,25 943,25 1141,373 943,720 537,720 339,373" fill="none" stroke="url(#gold-sheen)" stroke-width="3"/>
    <polygon class="hex-honeycomb" role="img" aria-label="Textura de panal de abeja en tonos negros" points="541,31 939,31 1134,373 939,714 541,714 346,373" fill="#111111"/>

    <!-- brand -->
    <circle class="brand-dot" cx="740" cy="140" r="40" fill="none" stroke="url(#gold-sheen)" stroke-width="6"/>
    <text class="brand-name" x="745" y="248" text-anchor="middle">VORET</text>

    <!-- title -->
    <text class="product-title" x="748" y="392" text-anchor="middle">MIEL DE AGAVE</text>
    <text class="product-title" x="748" y="464" text-anchor="middle">KOSHER</text>

    <!-- certification seal -->
    <circle class="certificate-seal" cx="740" cy="582" r="75" fill="url(#gold-sheen)"/>
    <circle class="certificate-seal-core" cx="740" cy="582" r="58" style="fill: var(--label-black)"/>

    <text class="volume" x="740" y="700" text-anchor="middle">750ml</text>

    <!-- distributor -->
    <text class="distributor" x="32" y="616">Distributed by:</text>
    <text class="distributor" x="32" y="646">Voret, France</text>

    <!-- nutrition table -->
    <g class="nutrition-table">
      <rect x="1210" y="370" width="243" height="308" fill="none" style="stroke: var(--table-line)" stroke-width="1.5"/>
      <text class="nutrition-title" x="1331" y="400" text-anchor="middle">Declaración</text>
      <text class="nutrition-title" x="1331" y="426" text-anchor="middle">Nutrimental</text>

      <text class="nutrition-row strong" x="1220" y="463">Contenido energético por envase</text>
      <text class="nutrition-row nutrition-value" x="1445" y="463">2,050,kcal</text>
      <text class="nutrition-row nutrition-value" x="1445" y="477">8,639 kJ</text>
      <line x1="1218" y1="483" x2="1446" y2="483" style="stroke: var(--table-line)" stroke-width="1"/>

      <text class="nutrition-row" x="1220" y="495">Tamaño de la porción</text>
      <text class="nutrition-row nutrition-value" x="1445" y="495">100g</text>
      <text class="nutrition-row" x="1220" y="509">Porciones por envase</text>
      <text class="nutrition-row nutrition-value" x="1445" y="509">3.3</text>
      <text class="nutrition-row" x="1220" y="523">Contenido energético por porción</text>
      <text class="nutrition-row nutrition-value" x="1445" y="523">310 kcal</text>
      <text class="nutrition-row nutrition-value" x="1445" y="537">1,309 kJ</text>
      <line x1="1218" y1="543" x2="1446" y2="543" style="stroke: var(--table-line)" stroke-width="2.5"/>

      <text class="nutrition-row" x="1220" y="559">Proteinas</text>
      <text class="nutrition-row nutrition-value" x="1445" y="559">0 g</text>
      <text class="nutrition-row" x="1220" y="573">Grasas</text>
      <text class="nutrition-row nutrition-value" x="1445" y="573">0 g</text>
      <text class="nutrition-row" x="1245" y="587">Grasa saturada</text>
      <text class="nutrition-row nutrition-value" x="1445" y="587">0 g</text>
      <text class="nutrition-row" x="1245" y="601">Grasas trans</text>
      <text class="nutrition-row nutrition-value" x="1445" y="601">0 mg</text>
      <text class="nutrition-row" x="1220" y="615">Hidratos de carbona disponibles</text>
      <text class="nutrition-row nutrition-value" x="1445" y="615">77 g</text>
      <text class="nutrition-row" x="1245" y="629">Azucares</text>
      <text class="nutrition-row nutrition-value" x="1445" y="629">77 g</text>
      <text class="nutrition-row" x="1245" y="643">Azucares añadidas</text>
      <text class="nutrition-row nutrition-value" x="1445" y="643">0 g</text>
      <text class="nutrition-row" x="1220" y="657">Fibra dietetica</text>
      <text class="nutrition-row nutrition-value" x="1445" y="657">menos de 1 g</text>
      <text class="nutrition-row" x="1220" y="671">Sodio</text>
      <text class="nutrition-row nutrition-value" x="1445" y="671">0 mg</text>
    </g>
  </svg>
</main>
</body>
</html>
```